Outdoor sign for Brightwater Auto Restoration

I need a horizontal 4'x 8' outdoor roadside sign for my classic auto restoration business. I have uploaded colors and our logo. Needs the Brightwater name, a prominent Classic AUTO RESTORATION, phone number and website. We rebuild and restore vintage cars, trucks and 4x4s. I'd like something clean but possibly retro. Classic Auto Restoration is more important than the Brightwater name. It needs to be visible and readable from the street. NO CLIP ART

Target Market(s)

Customers who need their vintage care restored or upgraded. Men and women ages 25-75

Industry/Entity Type

Automotive

Colors
FFC000
F8CF3A
FAE287
FDF2CF
FEFAEE

Requirements
Must have
• Legible. Bright. Readable as a backlit 4' x 8' large horizontal sign (roughly 120cm X 240cm)
Nice to have
• Use of the Brightwater logo/type, Complete or Classic before prominent AUTO RESTORATION
Should not have
• Clip art of old cars or icons. And we don't want the Brightwater Logo from the website because it wont be legible from the road. I have included the Illustrator file for Brightwater text in the uploads

```html
<!DOCTYPE html>
<html lang="en">
<head>
<meta charset="utf-8">
<title>Brightwater Auto Restoration – Roadside Sign</title>
<link rel="stylesheet" href="https://fonts.googleapis.com/css2?family=Anton&family=League+Gothic&family=Archivo:wght@800&display=swap">
<style>
  :root {
    --sign-yellow: #FFC000;
    --sign-red: #D31B15;
    --sign-blue: #04557C;
    --sign-white: #FFFFFF;
  }
  html, body {
    margin: 0;
    padding: 0;
    width: 1200px;
    height: 600px;
    overflow: hidden;
    background: var(--sign-yellow);
  }
  .sign {
    display: block;
    width: 1200px;
    height: 600px;
  }
  .sign__sky { fill: var(--sign-yellow); }
  .sign__band { fill: var(--sign-blue); }

  .brand-name {
    font-family: "Anton", "Impact", sans-serif;
    font-size: 124px;
  }
  .brand-name--face { fill: var(--sign-red); stroke: var(--sign-white); stroke-width: 1; }
  .brand-name--shadow { fill: var(--sign-blue); }

  .headline {
    font-family: "League Gothic", "Oswald", sans-serif;
  }
  .headline--classic { font-size: 94px; }
  .headline--service { font-size: 268px; }
  .headline--face { fill: var(--sign-yellow); stroke: var(--sign-white); stroke-width: 1; }
  .headline--shadow { fill: var(--sign-red); }

  .contact {
    font-family: "Archivo", "Arial Black", sans-serif;
    font-weight: 800;
    font-size: 57px;
  }
  .contact--face { fill: var(--sign-yellow); stroke: var(--sign-white); stroke-width: 0.6; }
  .contact--shadow { fill: var(--sign-red); }

  .icon--face { fill: var(--sign-yellow); }
  .icon--shadow { fill: var(--sign-red); }
  .icon-line { fill: none; stroke: var(--sign-red); stroke-width: 2.4; }
</style>
</head>
<body>
<svg class="sign" viewBox="0 0 1200 600" xmlns="http://www.w3.org/2000/svg" role="img" aria-label="Brightwater Classic Auto Restoration sign">
  <!-- background -->
  <rect class="sign__sky" x="0" y="0" width="1200" height="600"/>
  <path class="sign__band" d="M0 223 L426 238 L426 195 Q426 172 449 172 L754 172 Q777 172 777 195 L777 238 L1200 223 L1200 600 L0 600 Z"/>

  <!-- business name -->
  <g class="brand">
    <text class="brand-name brand-name--shadow" x="297" y="152" textLength="620" lengthAdjust="spacingAndGlyphs" aria-hidden="true">BRIGHTWATER</text>
    <text class="brand-name brand-name--face" x="290" y="142" textLength="620" lengthAdjust="spacingAndGlyphs">BRIGHTWATER</text>
  </g>

  <!-- classic tag -->
  <g class="tagline">
    <text class="headline headline--classic headline--shadow" x="487" y="271" textLength="231" lengthAdjust="spacingAndGlyphs" aria-hidden="true">CLASSIC</text>
    <text class="headline headline--classic headline--face" x="483" y="266" textLength="231" lengthAdjust="spacingAndGlyphs">CLASSIC</text>
  </g>

  <!-- main service line -->
  <g class="service">
    <text class="headline headline--service headline--shadow" x="46" y="480" textLength="1120" lengthAdjust="spacingAndGlyphs" aria-hidden="true">AUTO RESTORATION</text>
    <text class="headline headline--service headline--face" x="40" y="470" textLength="1120" lengthAdjust="spacingAndGlyphs">AUTO RESTORATION</text>
  </g>

  <!-- phone -->
  <g class="contact-phone">
    <g transform="translate(42 504)">
      <path class="icon--shadow" transform="translate(3 4)" d="M12 0 Q0 4 0 22 Q0 40 12 46 L17 46 Q20 45 19 41 L17 35 Q16 32 13 33 Q9 30 9 22 Q9 14 13 11 Q16 12 17 9 L19 4 Q20 0 17 0 Z"/>
      <path class="icon--face" d="M12 0 Q0 4 0 22 Q0 40 12 46 L17 46 Q20 45 19 41 L17 35 Q16 32 13 33 Q9 30 9 22 Q9 14 13 11 Q16 12 17 9 L19 4 Q20 0 17 0 Z"/>
    </g>
    <text class="contact contact--shadow" x="78" y="552" textLength="292" lengthAdjust="spacingAndGlyphs" aria-hidden="true">501-555-0142</text>
    <text class="contact contact--face" x="75" y="548" textLength="292" lengthAdjust="spacingAndGlyphs">501-555-0142</text>
  </g>

  <!-- website -->
  <g class="contact-web">
    <circle class="icon--shadow" cx="485" cy="530" r="24"/>
    <circle class="icon--face" cx="482" cy="527" r="24"/>
    <g class="icon-line">
      <circle cx="482" cy="527" r="20"/>
      <ellipse cx="482" cy="527" rx="9" ry="20"/>
      <line x1="482" y1="507" x2="482" y2="547"/>
      <line x1="462" y1="527" x2="502" y2="527"/>
      <line x1="466" y1="516" x2="498" y2="516"/>
      <line x1="466" y1="538" x2="498" y2="538"/>
    </g>
    <text class="contact contact--shadow" x="522" y="552" textLength="640" lengthAdjust="spacingAndGlyphs" aria-hidden="true">BRIGHTWATERAUTOWORKS.COM</text>
    <text class="contact contact--face" x="518" y="548" textLength="640" lengthAdjust="spacingAndGlyphs">BRIGHTWATERAUTOWORKS.COM</text>
  </g>
</svg>
</body>
</html>
```